Stationary for 2-office law firm with global theme

I need stationary with contact info for two offices. I'd like the same letterhead design to work for printing on stationary and also for digital use in Word. The colors and feel should match the new logo, which is a stylized globe with and "F" in it. I'd also like envelopes with an eye-catching design.

Target Market(s)

U.S. citizens seeking dual citizenship with Italy or Ireland

Industry/Entity Type

Law

Font styles to use
Serif
Sans Serif
Other font styles liked:
• To match the logo?

Colors
0054AA
0677BA
7BADD7
CADEEF
E8F1F8

Requirements
Must have
• Clean, modern design incorporating new logo

```html
<!DOCTYPE html>
<html lang="en">
<head>
<meta charset="utf-8">
<title>Marvale Law — Stationery</title>
<link rel="stylesheet" href="https://fonts.googleapis.com/css2?family=Montserrat:wght@500;700&display=swap">
<style>
  :root {
    --sky: #00a9ec;
    --navy: #033f72;
    --navy-soft: #0d4a80;
    --blue: #0a93da;
    --ink: #1b2634;
    --paper: #ffffff;
    --ghost: #f3f5f7;
  }
  * { box-sizing: border-box; margin: 0; padding: 0; }
  html, body { width: 1200px; height: 3200px; overflow: hidden; }
  body {
    position: relative;
    background: var(--sky);
    font-family: "Montserrat", Arial, sans-serif;
  }
  .sheet {
    position: absolute;
    overflow: hidden;
    box-shadow: 0 14px 30px rgba(0, 40, 80, 0.22);
  }
  .sheet--white { background: var(--paper); }
  .sheet--navy { background: var(--navy); }

  .ghost-circle {
    position: absolute;
    border-radius: 50%;
    background: var(--ghost);
  }
  .sheet--navy .ghost-circle { background: var(--navy-soft); }

  .brand {
    position: absolute;
    display: flex;
    align-items: center;
    gap: 14px;
  }
  .brand__dot {
    width: 48px; height: 48px;
    border-radius: 50%;
    background: var(--blue);
    flex: none;
  }
  .brand__name {
    font-weight: 700;
    font-size: 30px;
    letter-spacing: 1px;
    color: var(--navy);
    text-transform: uppercase;
    white-space: nowrap;
  }
  .sheet--navy .brand__name { color: var(--paper); }
  .sheet--navy .brand__dot { background: #3fb6f0; }

  .contact {
    position: absolute;
    font-size: 13px;
    font-weight: 500;
    color: var(--ink);
    line-height: 1.55;
  }
  .contact__firm {
    font-weight: 700;
    font-size: 15px;
    color: var(--blue);
    text-transform: uppercase;
    margin-bottom: 2px;
  }
  .contact__row { display: flex; align-items: center; gap: 7px; }
  .contact__row svg { width: 12px; height: 12px; flex: none; fill: var(--blue); }

  .band { position: absolute; }
  .band--blue { background: var(--blue); }
  .band--navy { background: var(--navy); }
  .band--sky { background: #12a5e8; }

  /* envelope pair */
  .envelope-back { left: 250px; top: 470px; width: 800px; height: 400px; }
  .envelope-front { left: 130px; top: 90px; width: 800px; height: 400px; }
  .envelope-front .flap-strip { position: absolute; left: 0; top: 0; width: 100%; height: 54px; background: var(--sky); }

  /* letterhead with folder */
  .folder { left: 500px; top: 1330px; width: 560px; height: 780px; }
  .letterhead-mid { left: 120px; top: 1090px; width: 560px; height: 780px; }

  /* letterhead stack */
  .letter-under { left: 340px; top: 2330px; width: 600px; height: 820px; }
  .letter-top { left: 310px; top: 2300px; width: 600px; height: 820px; }
</style>
</head>
<body>

  <!-- Envelope back -->
  <section class="sheet sheet--navy envelope-back" aria-label="Envelope back">
    <div class="ghost-circle" style="left:300px; top:-40px; width:460px; height:460px;"></div>
    <div class="brand" style="left:250px; top:170px;">
      <span class="brand__dot"></span><span class="brand__name">Marvale Law</span>
    </div>
    <div class="band band--sky" style="left:0; bottom:0; width:380px; height:16px;"></div>
  </section>

  <!-- Envelope front -->
  <section class="sheet sheet--white envelope-front" aria-label="Envelope front">
    <div class="flap-strip"></div>
    <div class="ghost-circle" style="left:300px; top:40px; width:420px; height:420px;"></div>
    <div class="contact" style="left:34px; top:250px;">
      <p class="contact__firm">Marvale Law PLLC</p>
      <p class="contact__row"><svg viewBox="0 0 12 12"><path d="M2.5 1h2l1 3-1.3 1a6.5 6.5 0 0 0 2.8 2.8L8 6.5l3 1v2a1.5 1.5 0 0 1-1.5 1.5A8.5 8.5 0 0 1 1 2.5 1.5 1.5 0 0 1 2.5 1z"/></svg>(555) 014-2290</p>
      <p class="contact__row"><svg viewBox="0 0 12 12"><path d="M1 2.5h10v7H1z M1.5 3l4.5 3.5L10.5 3" fill="none" stroke="#0a93da" stroke-width="1.2"/></svg>info@marvalelaw.com</p>
      <p class="contact__row"><svg viewBox="0 0 12 12"><circle cx="6" cy="6" r="4.8" fill="none" stroke="#0a93da" stroke-width="1.2"/><path d="M1.2 6h9.6M6 1.2v9.6" stroke="#0a93da" stroke-width="1"/></svg>www.marvalelaw.com</p>
    </div>
    <div class="brand" style="right:40px; top:290px;">
      <span class="brand__dot"></span><span class="brand__name">Marvale Law</span>
    </div>
    <div class="band band--blue" style="left:0; bottom:0; width:300px; height:12px;"></div>
  </section>

  <!-- Folder -->
  <section class="sheet sheet--navy folder" aria-label="Folder cover">
    <div class="ghost-circle" style="left:120px; top:150px; width:520px; height:520px;"></div>
    <div class="brand" style="left:220px; top:160px;">
      <span class="brand__dot"></span><span class="brand__name">Marvale Law</span>
    </div>
    <div class="band band--sky" style="left:0; bottom:50px; width:300px; height:18px;"></div>
  </section>

  <!-- Letterhead over folder -->
  <section class="sheet sheet--white letterhead-mid" aria-label="Letterhead">
    <div class="ghost-circle" style="left:80px; top:200px; width:420px; height:420px;"></div>
    <div class="brand" style="right:40px; top:60px;">
      <span class="brand__dot"></span><span class="brand__name">Marvale Law</span>
    </div>
    <div class="contact" style="left:36px; top:650px;">
      <p class="contact__firm">Marvale Law PLLC</p>
      <p class="contact__row"><svg viewBox="0 0 12 12"><path d="M2.5 1h2l1 3-1.3 1a6.5 6.5 0 0 0 2.8 2.8L8 6.5l3 1v2a1.5 1.5 0 0 1-1.5 1.5A8.5 8.5 0 0 1 1 2.5 1.5 1.5 0 0 1 2.5 1z"/></svg>(555) 014-2290</p>
      <p class="contact__row"><svg viewBox="0 0 12 12"><path d="M1 2.5h10v7H1z M1.5 3l4.5 3.5L10.5 3" fill="none" stroke="#0a93da" stroke-width="1.2"/></svg>info@marvalelaw.com</p>
      <p class="contact__row"><svg viewBox="0 0 12 12"><circle cx="6" cy="6" r="4.8" fill="none" stroke="#0a93da" stroke-width="1.2"/><path d="M1.2 6h9.6M6 1.2v9.6" stroke="#0a93da" stroke-width="1"/></svg>www.marvalelaw.com</p>
    </div>
    <div class="band band--blue" style="left:0; bottom:0; width:220px; height:12px;"></div>
    <div class="band band--navy" style="left:230px; bottom:0; width:330px; height:12px;"></div>
  </section>

  <!-- Second page beneath -->
  <section class="sheet sheet--white letter-under" aria-label="Letterhead second page">
    <div class="band band--blue" style="left:0; bottom:0; width:240px; height:14px;"></div>
    <div class="band band--navy" style="left:250px; bottom:0; width:350px; height:14px;"></div>
  </section>

  <!-- Letterhead top page -->
  <section class="sheet sheet--white letter-top" aria-label="Letterhead">
    <div class="ghost-circle" style="left:90px; top:230px; width:440px; height:440px;"></div>
    <div class="brand" style="right:40px; top:64px;">
      <span class="brand__dot"></span><span class="brand__name">Marvale Law</span>
    </div>
    <div class="contact" style="left:36px; top:690px;">
      <p class="contact__firm">Marvale Law PLLC</p>
      <p class="contact__row"><svg viewBox="0 0 12 12"><path d="M2.5 1h2l1 3-1.3 1a6.5 6.5 0 0 0 2.8 2.8L8 6.5l3 1v2a1.5 1.5 0 0 1-1.5 1.5A8.5 8.5 0 0 1 1 2.5 1.5 1.5 0 0 1 2.5 1z"/></svg>(555) 014-2290</p>
      <p class="contact__row"><svg viewBox="0 0 12 12"><path d="M1 2.5h10v7H1z M1.5 3l4.5 3.5L10.5 3" fill="none" stroke="#0a93da" stroke-width="1.2"/></svg>info@marvalelaw.com</p>
      <p class="contact__row"><svg viewBox="0 0 12 12"><circle cx="6" cy="6" r="4.8" fill="none" stroke="#0a93da" stroke-width="1.2"/><path d="M1.2 6h9.6M6 1.2v9.6" stroke="#0a93da" stroke-width="1"/></svg>www.marvalelaw.com</p>
    </div>
    <div class="band band--blue" style="left:0; bottom:0; width:240px; height:12px;"></div>
    <div class="band band--navy" style="left:250px; bottom:0; width:350px; height:12px;"></div>
  </section>

</body>
</html>
```